Home care agency

Current website QRVCAREPLUS.com. Need to update and reformat to different pages. use my info from my current website

Target Market(s)

adult children

Industry/Entity Type

Home Health

Coding

Coded - Design and coding required

Number of Pages Required

4 page

Font styles to use
Sans Serif

Colors
3276b5
33a6d7
3277b5
85cae6
85acd3

```html
<!DOCTYPE html>
<html lang="en">
<head>
<meta charset="utf-8">
<title>QRV Care Plus – Home</title>
<link rel="stylesheet" href="https://fonts.googleapis.com/css2?family=Anton&family=Bebas+Neue&family=Great+Vibes&display=block">
<style>
  :root {
    --brand-blue: #3276b5;
    --brand-sky: #33a6d7;
    --brand-light: #85cae6;
    --brand-soft: #85acd3;
    --white: #ffffff;
    --logo-grey: #7d7d7d;
  }
  * { margin: 0; padding: 0; box-sizing: border-box; }
  html, body { width: 1200px; height: 675px; overflow: hidden; }
  body { position: relative; font-family: "Bebas Neue", sans-serif; background: #2b241f; }

  .hero-photo {
    position: absolute; inset: 0 0 13px 0;
    background:
      linear-gradient(90deg, rgba(110,105,100,.45) 0%, rgba(60,52,46,.1) 22%, rgba(0,0,0,0) 40%, rgba(90,85,80,.35) 80%, rgba(50,44,40,.3) 100%),
      linear-gradient(180deg, #4a4039 0%, #3b322c 45%, #2c241f 100%);
  }

  .logo-tab {
    position: absolute; left: 225px; top: 0; width: 175px; height: 178px;
    background: var(--white);
    border-radius: 0 0 88px 88px;
    display: flex; flex-direction: column; align-items: center; justify-content: center;
    color: var(--logo-grey); text-align: center;
  }
  .logo-name { font-size: 28px; line-height: 1; letter-spacing: 1.5px; }

  .main-nav { position: absolute; top: 0; left: 757px; display: flex; }
  .nav-item {
    height: 51px; padding: 0 11px; display: flex; align-items: center;
    color: var(--white); font-size: 12px; text-decoration: none; letter-spacing: .2px;
    margin-right: 17px;
  }
  .nav-item.is-active {
    background: var(--white); color: var(--brand-blue);
    border-radius: 0 0 22px 22px;
  }

  .hero-copy {
    position: absolute; left: 0; right: 0; top: 318px;
    text-align: center; color: var(--white);
  }
  .hero-script {
    font-family: "Great Vibes", "Brush Script MT", cursive;
    font-size: 62px; line-height: 64px; height: 64px;
  }
  .hero-title {
    font-family: "Anton", "Bebas Neue", sans-serif; font-weight: 400;
    font-size: 42px; line-height: 46px; margin-top: 2px;
    display: inline-block; transform: scaleX(.88); transform-origin: center;
  }
  .hero-actions { margin-top: 18px; }
  .hero-button {
    display: inline-block; width: 105px; height: 30px;
    border: 1px solid rgba(255,255,255,.85); border-radius: 3px;
    color: var(--white); font-size: 17px; letter-spacing: 2px; line-height: 29px; text-decoration: none;
  }

  .footer-band { position: absolute; left: 0; right: 0; bottom: 0; height: 13px; background: var(--brand-blue); }
</style>
</head>
<body>
  <div class="hero-photo" role="img" aria-label="Caregiver in a white coat smiling at a seated older man in a living room with a lamp and wooden side table"></div>

  <div class="logo-tab">
    <span class="logo-name">QRV Care Plus</span>
  </div>

  <nav class="main-nav">
    <a class="nav-item is-active" href="#">Home</a>
    <a class="nav-item" href="#">About Us</a>
    <a class="nav-item" href="#">Services</a>
    <a class="nav-item" href="#">Contact</a>
  </nav>

  <section class="hero-copy">
    <p class="hero-script">Providing Care</p>
    <h1 class="hero-title">Throughout the South Shore</h1>
    <div class="hero-actions"><a class="hero-button" href="#">Learn More</a></div>
  </section>

  <div class="footer-band"></div>
</body>
</html>
```